Boutique custom software development company needs new business card

Our nearly 20 year old custom software development company would like to better include the fact that we are now providing Bitcoin services. These new services are B2B include education (how to acquire and securely hold Bitcoin) and integrating Bitcoin payments into existing ecommerce sites or other existing systems. Please keep the card clean and simple. Attached is our current design and some other files. vexalon.example

Target Market(s)

businesses owners interested in long term relationship

Industry/Entity Type

Custom software development and Bitcoin

Contact Information for Business Card

Marcus Ellwood, marcus@vexalon.example, vexalon.example, (888) 555-VEXAL

Font styles to use
Other font styles liked:
• monospace

Requirements
Must have
• double-sided
Nice to have
• clean and simple
Should not have
• physical address

```html
<!DOCTYPE html>
<html lang="en">
<head>
<meta charset="utf-8">
<title>Vexalon Business Card</title>
<link href="https://fonts.googleapis.com/css2?family=Montserrat:wght@500;700;800&family=Lato:wght@400&display=swap" rel="stylesheet">
<style>
  :root {
    --brand-blue: #3f73b8;
    --brand-orange: #ef7a22;
    --ink: #111111;
    --paper: #ffffff;
    --backdrop: #eef1f6;
  }
  * { margin: 0; padding: 0; box-sizing: border-box; }
  html, body { width: 1200px; height: 1200px; overflow: hidden; background: var(--backdrop); }
  .canvas { position: relative; width: 1200px; height: 1200px; }
  .card { position: absolute; left: 237px; width: 726px; height: 419px; overflow: hidden; }
  .card--front { top: 86px; background: var(--paper); }
  .card--back { top: 690px; background: var(--brand-blue); }

  .wordmark {
    position: absolute; left: 0; right: 0; text-align: center;
    font-family: 'Montserrat', sans-serif; font-weight: 800; letter-spacing: 1px; line-height: 1;
  }
  .card--front .wordmark { top: 110px; font-size: 64px; color: var(--brand-blue); }
  .card--back .wordmark { top: 168px; font-size: 76px; color: var(--paper); }

  .tagline {
    position: absolute; left: 0; right: 0; text-align: center;
    font-family: 'Lato', sans-serif; font-weight: 400; letter-spacing: -0.6px; line-height: 1;
  }
  .card--front .tagline { top: 172px; font-size: 20px; color: var(--brand-blue); }
  .card--back .tagline { top: 236px; font-size: 24px; color: var(--paper); }

  .person { position: absolute; right: 337px; top: 240px; text-align: right; font-family: 'Montserrat', sans-serif; }
  .person__name { font-size: 36px; font-weight: 700; line-height: 1.1; white-space: nowrap; }
  .person__first { color: var(--brand-orange); }
  .person__last { color: var(--brand-blue); }
  .person__email { font-size: 17px; font-weight: 500; color: var(--ink); letter-spacing: 1px; margin-top: 2px; white-space: nowrap; }

  .divider { position: absolute; left: 418px; top: 247px; width: 2px; height: 54px; background: var(--brand-blue); }

  .contact { position: absolute; left: 438px; top: 244px; font-family: 'Montserrat', sans-serif; }
  .contact__row { display: flex; align-items: center; height: 34px; font-size: 18px; font-weight: 500; color: var(--ink); letter-spacing: 1px; white-space: nowrap; }
  .contact__icon { width: 22px; height: 22px; margin-right: 12px; flex: none; }

  .services-band {
    position: absolute; left: 0; top: 363px; width: 100%; height: 42px; background: var(--brand-blue);
    display: flex; align-items: center; justify-content: center;
    font-family: 'Montserrat', sans-serif; font-weight: 500; font-size: 19px; color: var(--paper); letter-spacing: 0.5px;
  }
  .accent-band { position: absolute; left: 0; top: 405px; width: 100%; height: 14px; background: var(--brand-orange); }
</style>
</head>
<body>
<div class="canvas">
  <section class="card card--front">
    <div class="wordmark">VEXALON</div>
    <div class="tagline">developer of custom applications</div>

    <div class="person">
      <div class="person__name"><span class="person__first">Marcus</span> <span class="person__last">Ellwood</span></div>
      <div class="person__email">marcus@vexalon.example</div>
    </div>

    <div class="divider"></div>

    <div class="contact">
      <div class="contact__row">
        <svg class="contact__icon" viewBox="0 0 24 24" fill="none" stroke="#3f73b8" stroke-width="1.6">
          <rect x="7" y="2" width="10" height="20" rx="1.5"/>
          <line x1="10" y1="4.5" x2="14" y2="4.5"/>
          <circle cx="12" cy="19" r="0.6" fill="#3f73b8"/>
        </svg>
        (888) 555-VEXAL
      </div>
      <div class="contact__row">
        <svg class="contact__icon" viewBox="0 0 24 24" fill="none" stroke="#3f73b8" stroke-width="1.4">
          <circle cx="12" cy="12" r="9.5"/>
          <ellipse cx="12" cy="12" rx="4.5" ry="9.5"/>
          <line x1="2.5" y1="12" x2="21.5" y2="12"/>
          <path d="M4 7h16M4 17h16"/>
        </svg>
        vexalon.example
      </div>
    </div>

    <div class="services-band">Bitcoin education &amp; payment integration</div>
    <div class="accent-band"></div>
  </section>

  <section class="card card--back">
    <div class="wordmark">VEXALON</div>
    <div class="tagline">developer of custom applications</div>
  </section>
</div>
</body>
</html>
```